Law Firm Website

We are looking to update our old, tired and very flat website. We have someone who will code and host the site but we need some design inspiration. The website will consist of no more than 2/3 pages, possibly with pop-ups for information. We already have all the blurb. We would like something distinctive, clean and eye-catching, using the purple and white theme that we already use on our firm stationery. Examples uploaded. Current website URL is www.holtandbrevis.example.

Industry/Entity Type

Law Firm

```html
<!DOCTYPE html>
<html lang="en">
<head>
<meta charset="utf-8">
<title>Peter Brevis — Holt + Brevis Solicitors</title>
<link rel="stylesheet" href="https://fonts.googleapis.com/css2?family=Open+Sans:wght@400;600;700&display=swap">
<style>
  :root {
    --purple: #564291;
    --purple-footer: #544593;
    --ink: #1d1d1d;
    --heading-grey: #767676;
    --muted: #a3a3a3;
    --white: #ffffff;
    --map-tone: #e6e3dc;
    --photo-dark: #3a3a3a;
    --photo-light: #bdbdbd;
  }
  * { box-sizing: border-box; margin: 0; padding: 0; }
  html, body { width: 1200px; height: 710px; overflow: hidden; }
  body {
    position: relative;
    background: var(--white);
    font-family: "Open Sans", Arial, sans-serif;
    color: var(--ink);
  }
  .top-band { position: absolute; left: 0; top: 0; width: 1200px; height: 11px; background: var(--purple); }

  .brand {
    position: absolute; left: 167px; top: 22px;
    font-size: 40px; font-weight: 600; letter-spacing: -0.5px;
    color: var(--ink); line-height: 1;
  }

  .call-line {
    position: absolute; right: 165px; top: 33px;
    font-size: 13px; font-weight: 600; color: var(--ink); letter-spacing: 0.1px;
    display: flex; align-items: center; gap: 6px; white-space: nowrap;
  }
  .call-line .plus { width: 11px; height: 11px; }

  .main-nav {
    position: absolute; right: 165px; top: 69px;
    display: flex; gap: 31px; font-size: 13.5px; white-space: nowrap;
  }
  .main-nav a { color: var(--ink); text-decoration: none; position: relative; }
  .main-nav a.is-current { color: var(--purple); font-weight: 600; }
  .main-nav a.is-current::after {
    content: ""; position: absolute; left: 0; right: 0; top: 24px;
    height: 3px; background: var(--purple);
  }

  .section-title {
    position: absolute; font-size: 22px; font-weight: 600; color: var(--heading-grey);
    letter-spacing: 0.5px; padding-bottom: 7px; border-bottom: 1px solid var(--purple);
  }
  .profile-title { left: 167px; top: 146px; width: 494px; }
  .contact-title { left: 763px; top: 148px; width: 272px; text-align: right; }

  .portrait {
    position: absolute; left: 166px; top: 197px; width: 137px; height: 137px;
    background: linear-gradient(135deg, var(--photo-light), var(--photo-dark));
  }
  .bio {
    position: absolute; left: 316px; top: 195px; width: 345px;
    font-size: 13px; line-height: 16.6px;
  }
  .bio p { margin-bottom: 16.6px; }

  .map { position: absolute; left: 763px; width: 121px; height: 121px; background: var(--map-tone); }
  .map-primary { top: 198px; }
  .map-secondary { top: 342px; opacity: 0.8; }

  .office {
    position: absolute; left: 911px; width: 124px; font-size: 12.2px; line-height: 18.5px;
    white-space: nowrap;
  }
  .office p + p { margin-top: 9px; }
  .office-primary { top: 195px; color: var(--ink); }
  .office-secondary { top: 337px; color: var(--muted); }

  .cta {
    position: absolute; left: 763px; top: 481px; width: 284px; height: 59px;
    background: var(--purple); color: var(--white); padding: 6px 14px;
  }
  .cta-head { font-size: 22px; line-height: 26px; display: flex; align-items: center; gap: 8px; }
  .cta-head svg { width: 17px; height: 17px; }
  .cta-sub { font-size: 16.5px; font-weight: 600; line-height: 20px; }

  .site-footer {
    position: absolute; left: 0; top: 588px; width: 1200px; height: 122px;
    background: var(--purple-footer); color: var(--white);
  }
  .footer-brand { position: absolute; left: 165px; top: 8px; font-size: 17px; font-weight: 600; letter-spacing: -0.3px; }
  .footer-about { position: absolute; left: 165px; top: 38px; width: 270px; font-size: 11px; font-weight: 600; line-height: 14.5px; }
  .footer-about p + p { margin-top: 6px; }
  .footer-rules { position: absolute; left: 464px; top: 38px; width: 260px; font-size: 11px; font-weight: 600; line-height: 14.5px; }
  .partner-badge { position: absolute; left: 898px; top: 0; width: 150px; height: 49px; background: var(--white); }
  .partner-badge span { position: absolute; left: 14px; top: 13px; width: 22px; height: 22px; background: var(--purple); }
  .legal-line {
    position: absolute; right: 166px; top: 101px;
    font-size: 9.5px; font-weight: 700; letter-spacing: 0.2px; white-space: nowrap;
  }
</style>
</head>
<body>
  <div class="top-band"></div>

  <header>
    <div class="brand">Holt + Brevis</div>
    <div class="call-line">
      <span>CALL US NOW: DANIEL HOLT&nbsp; 0333 555 0142</span>
      <svg class="plus" viewBox="0 0 10 10" aria-hidden="true"><path d="M3.6 0h2.8v3.6H10v2.8H6.4V10H3.6V6.4H0V3.6h3.6z" fill="#564291"/></svg>
      <span>PETER BREVIS&nbsp; 0845 555 0187</span>
    </div>
    <nav class="main-nav">
      <a href="#">Home</a>
      <a href="#">Areas of Expertise</a>
      <a href="#">Daniel Holt</a>
      <a href="#" class="is-current">Peter Brevis</a>
      <a href="#">Contact</a>
    </nav>
  </header>

  <main>
    <h1 class="section-title profile-title">PETER BREVIS</h1>
    <div class="portrait" role="img" aria-label="Black and white portrait photograph of Peter Brevis"></div>
    <div class="bio">
      <p>Peter Brevis has 40 years experience in<br>the law.</p>
      <p>He qualified in the City of London where he worked for many years and then set up his own firm in 1981 and then going on to join a larger commercial practice for 2 years.</p>
      <p>He has a wide range of expertise in commercial and private client matters.</p>
    </div>

    <h2 class="section-title contact-title">CONTACT US</h2>

    <div class="map map-primary" role="img" aria-label="Street map showing the Larkfield office location"></div>
    <div class="office office-primary">
      <p>PETER BREVIS<br>14B The Crescent<br>Larkfield<br>Hertfordshire AL9 4ZZ</p>
      <p>Tel: 0845 555 0187<br>Fax: 020 7946 0318</p>
    </div>

    <div class="map map-secondary" role="img" aria-label="Street map showing the Ashgrove office location"></div>
    <div class="office office-secondary">
      <p>DANIEL HOLT<br>22d Elmcote Hill<br>Ashgrove<br>London N99 9ZX</p>
      <p>Tel: 0333 555 0142<br>Fax: 020 7946 0422</p>
    </div>

    <div class="cta">
      <div class="cta-head">HAVE QUESTIONS?
        <svg viewBox="0 0 10 10" aria-hidden="true"><path d="M3.6 0h2.8v3.6H10v2.8H6.4V10H3.6V6.4H0V3.6h3.6z" fill="#ffffff"/></svg>
      </div>
      <div class="cta-sub">Contact us we are here to help.</div>
    </div>
  </main>

  <footer class="site-footer">
    <div class="footer-brand">Holt + Brevis</div>
    <div class="footer-about">
      <p>A firm of solicitors with offices in Ashgrove, London and Larkfield, Hertfordshire.</p>
      <p>This firm is authorised and regulated by the Legal Standards Authority, no.600981.</p>
    </div>
    <div class="footer-rules">
      <p>Professional rules can be viewed on www.legalstandards.example/code-of-conduct.</p>
    </div>
    <div class="partner-badge" role="img" aria-label="Partner membership badge"><span></span></div>
    <div class="legal-line">LEGAL NOTICES | PRIVACY POLICY | © HOLT &amp; BREVIS 2014 &nbsp;| &nbsp;VAT REGISTERED NUMBER: 912 4470 35</div>
  </footer>
</body>
</html>
```